Admin Backend Redesign

We need a redesign for our backend which supoosed to make the backoffice look more modern!

I will add screenshots of the backoffice so you know what data will be shown in the Admin.

Have in mind that the users of this backend are Doctors. We need a clinical look, modern and sharp. The backoffice is responsive, have that in mind. We need the backoffice to look as professional as possible.

The theme used for the website is: http://velmora.quillstack-sample.com/

ON the main page of the backoffice, under every widget i need some space to write an explanation what the widget is about.

The color code used in our logo and website is #57aad4 combined with white.

We are open for ideas!
Updates

Project Deadline Extended
Reason: Designs are ok, but nothing innovative. Please use more modern designs!

Project Deadline Extended
Reason: Havent recieved a perfect design yet. Please read instructions carefully! Thank you

Project Deadline Extended
Reason: Hey everybody, sorry for the delay. We will decide in 3 days. If anyone wants to add a Design, that would be great.

Target Market(s)

Doctors, therapists

Industry/Entity Type

It Professional

Font styles to use
Sans Serif

Requirements
Must have
• Must look uptodate, modern, like new back offices look nowadays

```html
<!DOCTYPE html>
<html lang="de">
<head>
<meta charset="utf-8">
<title>Praxora Admin – Dashboard</title>
<link href="https://fonts.googleapis.com/css2?family=Montserrat:wght@300;400;500;600&display=swap" rel="stylesheet">
<style>
:root{
  --brand:#57aad4;
  --navy:#36587b;
  --ink:#3a5a7c;
  --text:#6f7782;
  --muted:#a0a6ad;
  --page:#f2f2f2;
  --band:#e7e7e7;
  --white:#ffffff;
  --red:#ee5262;
  --red-dark:#e0293d;
  --cyan:#4dbde6;
  --cyan-dark:#26aee0;
  --teal:#3ccfa5;
  --line-blue:#2468a8;
}
*{box-sizing:border-box;margin:0;padding:0}
html,body{width:922px;height:1200px;overflow:hidden;background:var(--page)}
body{font-family:"Montserrat",Arial,sans-serif;color:var(--text)}
.stage{position:absolute;left:0;top:0;width:1152px;height:1500px;transform:scale(.8);transform-origin:0 0;background:var(--page)}
.abs{position:absolute}

/* sidebar */
.sidebar{position:absolute;left:0;top:0;width:269px;height:1500px;background:var(--navy);z-index:2}
.logo{position:absolute;left:40px;top:21px;font-size:21px;color:var(--brand);letter-spacing:.5px;font-weight:400}
.menu-toggle{position:absolute;left:251px;top:16px}
.nav{position:absolute;left:0;top:70px;width:269px;list-style:none}
.nav li{position:relative;height:46px;display:flex;align-items:center;border-bottom:1px solid rgba(255,255,255,.12);font-size:11px;font-weight:600;letter-spacing:1px;color:var(--brand)}
.nav li .icon{width:52px;height:100%;display:flex;align-items:center;justify-content:center;border-right:1px solid rgba(255,255,255,.12)}
.nav li .label{padding-left:12px;flex:1}
.nav li .count{width:14px;height:14px;border-radius:50%;background:#24415f;color:#fff;font-size:7px;display:flex;align-items:center;justify-content:center;margin-right:22px}
.nav li.active{background:var(--brand);color:#fff;margin-left:5px;border-bottom:none}
.nav li.active .icon{width:47px;border-right:1px solid rgba(255,255,255,.25)}
.nav li.active .count{background:#fff;color:var(--brand)}
.nav li.active::after{content:"";position:absolute;right:-9px;top:14px;border-left:9px solid var(--brand);border-top:9px solid transparent;border-bottom:9px solid transparent}

/* top bar */
.topbar{position:absolute;left:269px;top:0;width:883px;height:70px;background:var(--band)}
.user{position:absolute;right:22px;top:22px;display:flex;align-items:center;font-size:8.5px;color:var(--ink)}
.mail{position:relative;margin-right:44px}
.mail .badge{position:absolute;left:-13px;top:-1px;width:11px;height:11px;border-radius:50%;background:var(--red);color:#fff;font-size:7px;display:flex;align-items:center;justify-content:center}
.avatar{width:22px;height:22px;border-radius:50%;background:linear-gradient(#c98f72,#7a4a35);margin-right:9px}
.caret{margin-left:16px;color:var(--muted);font-size:8px}

.breadcrumb{position:absolute;left:293px;top:93px;width:838px;height:33px;background:#e4e4e4;clip-path:polygon(12px 0,calc(100% - 12px) 0,100% 50%,calc(100% - 12px) 100%,12px 100%,0 50%);display:flex;align-items:center;padding-left:20px;font-size:10px;color:var(--ink)}
.breadcrumb .sep{margin:0 10px;color:var(--muted);font-style:italic}
.breadcrumb .current{color:var(--muted)}
.breadcrumb .gear{position:absolute;right:14px;top:9px}

/* panels */
.panel{position:absolute;background:var(--white)}
.panel-head{height:44px;background:var(--band);display:flex;align-items:center;padding-left:16px;font-size:11.5px;color:var(--ink);letter-spacing:.5px}
.panel-head svg{margin-right:13px}
.note{position:absolute;font-size:6.5px;line-height:10.5px;color:var(--muted);padding-left:16px}
.note::before{content:"i";position:absolute;left:0;top:1px;width:8px;height:8px;border:1px solid #8a9097;border-radius:50%;font-size:6px;line-height:8px;text-align:center;color:#8a9097;font-weight:600}

.legend{position:absolute;font-size:7px;color:var(--ink);line-height:13px}
.legend i{display:inline-block;width:6px;height:6px;border-radius:50%;margin-right:6px;vertical-align:0}

/* action tiles */
.tile{position:absolute;width:120px;height:120px;color:#fff;text-align:center}
.tile h3{font-weight:400;font-size:15px;margin-top:4px}
.tile p{font-size:7.5px;opacity:.85;margin-top:1px}
.tile .foot{position:absolute;left:0;bottom:0;width:100%;height:20px;display:flex;align-items:center;justify-content:flex-end;padding-right:6px;font-size:7px;font-weight:600;letter-spacing:.5px}
.tile .foot span{margin-right:6px}
.tile-red{background:var(--red)}
.tile-red .foot{background:var(--red-dark)}
.tile-cyan{background:var(--cyan)}
.tile-cyan .foot{background:var(--cyan-dark)}

.welcome-text{position:absolute;left:20px;top:56px;width:224px;font-size:7.6px;line-height:12.7px;color:var(--text)}
.btn{position:absolute;background:var(--brand);color:#fff;font-size:7px;font-weight:600;border-radius:2px;display:flex;align-items:center;justify-content:center}

/* tables */
.search{position:absolute;height:23px;background:#f1f1f1;font-size:8px;color:var(--muted);display:flex;align-items:center;padding-left:10px}
.search svg{position:absolute;right:6px;top:4px}
.grid{position:absolute;border-collapse:collapse;font-size:8.3px}
.grid th{font-weight:400;color:var(--ink);text-align:left;height:26px;vertical-align:middle;font-size:8.5px}
.grid th .sort{display:inline-block;color:#c3c7cc;font-size:6px;line-height:4px;width:9px;vertical-align:middle;margin-right:2px}
.grid td{height:18.6px;border-top:1px solid #ececec;padding-left:7px;color:var(--muted)}
.grid td+td{border-left:1px solid #ececec}
.grid tbody tr:nth-child(odd) td{background:#f7f7f7}
.grid a{color:var(--brand);text-decoration:none}
.grid .chev{color:var(--ink);margin-right:6px;font-size:8px}
.grid td.stars{color:var(--ink);letter-spacing:-.5px;font-size:10px;font-weight:600}
.bar{width:116px;height:6px;background:#ebebeb;border-radius:3px;overflow:hidden}
.bar i{display:block;height:100%;background:var(--brand);border-radius:3px}
.entries{position:absolute;font-size:7.5px;color:var(--ink)}
.pager{position:absolute;display:flex;gap:4px}
.pager span{width:12px;height:12px;background:#eaeaea;font-size:6px;color:var(--brand);display:flex;align-items:center;justify-content:center}
.pager span.arrow{background:transparent;color:var(--ink);font-size:9px}
.pager span.active{background:#ddd;color:var(--ink)}
.pager span.next{background:var(--brand);color:#fff;font-size:9px}

.footer{position:absolute;left:269px;top:1458px;width:883px;height:42px;border-top:1px solid #e3e3e3}
.footer .copy{position:absolute;left:11px;top:16px;font-size:6.5px;color:var(--text)}
.footer .brand{position:absolute;right:20px;top:14px;font-size:10px;font-weight:600;color:var(--ink);letter-spacing:.5px}
</style>
</head>
<body>
<div class="stage">

  <aside class="sidebar">
    <div class="logo">Praxora Admin</div>
    <svg class="menu-toggle" width="36" height="40" viewBox="0 0 36 40">
      <polygon points="18,1 35,10.5 35,29.5 18,39 1,29.5 1,10.5" fill="#57aad4"/>
      <path d="M9 14h18M9 20h18M9 26h18" stroke="#fff" stroke-width="2"/>
    </svg>
    <ul class="nav">
      <li class="active">
        <span class="icon"><svg width="16" height="14" viewBox="0 0 16 14" fill="none" stroke="#fff" stroke-width="1.3"><path d="M1 7 8 1l7 6M3 6v7h4V9h2v4h4V6"/></svg></span>
        <span class="label">Dashboard</span><span class="count">1</span>
      </li>
      <li>
        <span class="icon"><svg width="12" height="15" viewBox="0 0 12 15" fill="none" stroke="#57aad4" stroke-width="1.2"><circle cx="6" cy="4" r="3"/><path d="M1 14v-4h10v4z"/></svg></span>
        <span class="label">Mein Konto</span><span class="count">0</span>
      </li>
      <li>
        <span class="icon"><svg width="18" height="13" viewBox="0 0 18 13" fill="none" stroke="#57aad4" stroke-width="1.1"><circle cx="9" cy="4" r="2.5"/><circle cx="3.5" cy="5" r="2"/><circle cx="14.5" cy="5" r="2"/><path d="M4.5 12a4.5 4 0 0 1 9 0M0.5 11a3 3 0 0 1 4-2.5M17.5 11a3 3 0 0 0-4-2.5"/></svg></span>
        <span class="label">Patientenbewertungen</span><span class="count">1</span>
      </li>
    </ul>
  </aside>

  <header class="topbar">
    <div class="user">
      <span class="mail"><span class="badge">1</span>
        <svg width="14" height="10" viewBox="0 0 14 10" fill="none" stroke="#57aad4" stroke-width="1.1"><rect x=".5" y=".5" width="13" height="9"/><path d="M.5 .5 7 6l6.5-5.5"/></svg>
      </span>
      <span class="avatar" role="img" aria-label="Profilfoto der angemeldeten Nutzerin"></span>
      <span>Mara Lindqvist</span>
      <span class="caret">▼</span>
    </div>
  </header>

  <nav class="breadcrumb">
    <svg width="13" height="11" viewBox="0 0 16 14" fill="none" stroke="#3a5a7c" stroke-width="1.4" style="margin-right:6px"><path d="M1 7 8 1l7 6M3 6v7h4V9h2v4h4V6"/></svg>
    <span>Home</span><span class="sep">//</span><span class="current">Dashboard</span>
    <svg class="gear" width="15" height="15" viewBox="0 0 16 16" fill="none" stroke="#a0a6ad" stroke-width="1.3"><circle cx="8" cy="8" r="2.5"/><circle cx="8" cy="8" r="5.5" stroke-dasharray="2.2 1.6"/></svg>
  </nav>

  <!-- trend chart -->
  <section class="panel" style="left:290px;top:150px;width:552px;height:307px">
    <div class="panel-head">
      <svg width="16" height="16" viewBox="0 0 16 16" fill="none" stroke="#57aad4" stroke-width="1.3"><path d="M1 1v14h14M4 11l4-4 2 2 5-5M11 4h4v4"/></svg>Rankora Tren Fur:
    </div>
    <div class="legend" style="left:415px;top:51px">
      <div><i style="background:#7bd24a"></i>ipsum dolor sit amet</div>
      <div><i style="background:var(--line-blue)"></i>consectetur adipiscing elit</div>
    </div>
    <svg class="abs" style="left:0;top:44px" width="552" height="263" viewBox="290 194 552 263">
      <g stroke="#ededed" stroke-width="1">
        <path d="M350 249H817M350 278H817M350 306H817M350 335H817M350 364H817M350 393H817M350 415H817"/>
        <path d="M350 249V415M392 249V415M425 249V415M458 249V415M492 249V415M525 249V415M558 249V415M592 249V415M625 249V415M658 249V415M692 249V415M725 249V415M758 249V415M792 249V415M817 249V415"/>
      </g>
      <g font-family="Montserrat, sans-serif" font-size="9" fill="#3a5a7c" text-anchor="end">
        <text x="338" y="252">30</text><text x="338" y="281">25</text><text x="338" y="310">20</text><text x="338" y="339">15</text><text x="338" y="367">10</text><text x="338" y="396">5</text><text x="338" y="425">0</text>
      </g>
      <g font-family="Montserrat, sans-serif" font-size="9" fill="#3a5a7c" text-anchor="middle">
        <text x="384" y="430">Oct 2012</text><text x="453" y="430">Jan 2013</text><text x="523" y="430">Apr 2013</text><text x="591" y="430">Jul 2013</text><text x="659" y="430">Oct 2013</text><text x="729" y="430">Jan 2014</text><text x="798" y="430">Apr 2014</text>
      </g>
      <polyline fill="none" stroke="#3ccfa5" stroke-width="3" points="350,313 460,345 553,295 648,325 735,295 815,282"/>
      <polyline fill="none" stroke="#2468a8" stroke-width="3" points="350,403 432,383 513,392 617,362 676,348 710,279 789,263 817,251"/>
      <g fill="#3ccfa5" stroke="#fff" stroke-width="2">
        <circle cx="350" cy="313" r="6"/><circle cx="460" cy="345" r="6"/><circle cx="553" cy="295" r="6"/><circle cx="648" cy="325" r="6"/><circle cx="735" cy="295" r="6"/><circle cx="815" cy="282" r="6"/>
      </g>
      <g fill="#2468a8" stroke="#fff" stroke-width="2">
        <circle cx="350" cy="403" r="6"/><circle cx="432" cy="383" r="6"/><circle cx="513" cy="392" r="6"/><circle cx="617" cy="362" r="6"/><circle cx="676" cy="348" r="6"/><circle cx="710" cy="279" r="6"/><circle cx="789" cy="263" r="6"/><circle cx="817" cy="251" r="6"/>
      </g>
    </svg>
  </section>
  <p class="note" style="left:290px;top:469px;width:540px">Lorem ipsum dolor sit amet, consectetuer adipiscing elit, sed diam nonummy nibh euismod tincidunt sit amet, consectetuer adipiscing elit sit amet, consectetuer adipiscing elit.</p>

  <!-- pie 1 -->
  <section class="panel" style="left:290px;top:512px;width:264px;height:227px">
    <div class="panel-head">
      <svg width="15" height="15" viewBox="0 0 16 16" fill="none" stroke="#57aad4" stroke-width="1.3"><circle cx="8" cy="8" r="6.5"/><path d="M8 1.5V8h6.5"/></svg>Pie 1:
    </div>
    <div class="legend" style="left:212px;top:58px">
      <div><i style="background:#fde27a"></i>Series</div><div><i style="background:#4fc0e8"></i>Series</div><div><i style="background:#ee5262"></i>Series</div>
    </div>
    <svg class="abs" style="left:35px;top:68px" width="132" height="132" viewBox="0 0 132 132">
      <g transform="rotate(-90 66 66)" fill="none">
        <circle cx="66" cy="66" r="61" stroke="#fde27a" stroke-width="10" pathLength="100" stroke-dasharray="41.7 100"/>
        <circle cx="66" cy="66" r="61" stroke="#4fc0e8" stroke-width="10" pathLength="100" stroke-dasharray="18 100" stroke-dashoffset="-41.7"/>
        <circle cx="66" cy="66" r="61" stroke="#ee5262" stroke-width="10" pathLength="100" stroke-dasharray="40.3 100" stroke-dashoffset="-59.7"/>
        <circle cx="66" cy="66" r="28" stroke="#feeca6" stroke-width="56" pathLength="100" stroke-dasharray="41.7 100"/>
        <circle cx="66" cy="66" r="28" stroke="#86d3f0" stroke-width="56" pathLength="100" stroke-dasharray="18 100" stroke-dashoffset="-41.7"/>
        <circle cx="66" cy="66" r="28" stroke="#f28c96" stroke-width="56" pathLength="100" stroke-dasharray="40.3 100" stroke-dashoffset="-59.7"/>
      </g>
    </svg>
  </section>
  <p class="note" style="left:290px;top:751px;width:264px">Lorem ipsum dolor sit amet, consectetuer adipiscing elit, sed diam nonummy nibh euismod tincidunt sit amet, consectetuer adipiscing elit sit amet, consectetuer adipiscing elit.</p>

  <!-- pie 2 -->
  <section class="panel" style="left:579px;top:512px;width:263px;height:227px">
    <div class="panel-head">
      <svg width="15" height="15" viewBox="0 0 16 16" fill="none" stroke="#57aad4" stroke-width="1.3"><circle cx="8" cy="8" r="6.5"/><path d="M8 1.5V8h6.5"/></svg>Pie 2:
    </div>
    <div class="legend" style="left:211px;top:58px">
      <div><i style="background:#fde27a"></i>Series</div><div><i style="background:#4fc0e8"></i>Series</div><div><i style="background:#ee5262"></i>Series</div><div><i style="background:#3ccfa5"></i>Series</div><div><i style="background:#9b6fc0"></i>Series</div>
    </div>
    <svg class="abs" style="left:40px;top:68px" width="132" height="132" viewBox="0 0 132 132">
      <g transform="rotate(-90 66 66)" fill="none">
        <circle cx="66" cy="66" r="61" stroke="#fde27a" stroke-width="10" pathLength="100" stroke-dasharray="7 100"/>
        <circle cx="66" cy="66" r="61" stroke="#4fc0e8" stroke-width="10" pathLength="100" stroke-dasharray="8 100" stroke-dashoffset="-7"/>
        <circle cx="66" cy="66" r="61" stroke="#ee5262" stroke-width="10" pathLength="100" stroke-dasharray="31 100" stroke-dashoffset="-15"/>
        <circle cx="66" cy="66" r="61" stroke="#3ccfa5" stroke-width="10" pathLength="100" stroke-dasharray="28 100" stroke-dashoffset="-46"/>
        <circle cx="66" cy="66" r="61" stroke="#9b6fc0" stroke-width="10" pathLength="100" stroke-dasharray="26 100" stroke-dashoffset="-74"/>
        <circle cx="66" cy="66" r="28" stroke="#feeca6" stroke-width="56" pathLength="100" stroke-dasharray="7 100"/>
        <circle cx="66" cy="66" r="28" stroke="#86d3f0" stroke-width="56" pathLength="100" stroke-dasharray="8 100" stroke-dashoffset="-7"/>
        <circle cx="66" cy="66" r="28" stroke="#f28c96" stroke-width="56" pathLength="100" stroke-dasharray="31 100" stroke-dashoffset="-15"/>
        <circle cx="66" cy="66" r="28" stroke="#7fddc5" stroke-width="56" pathLength="100" stroke-dasharray="28 100" stroke-dashoffset="-46"/>
        <circle cx="66" cy="66" r="28" stroke="#b89ad3" stroke-width="56" pathLength="100" stroke-dasharray="26 100" stroke-dashoffset="-74"/>
      </g>
    </svg>
  </section>
  <p class="note" style="left:579px;top:751px;width:264px">Lorem ipsum dolor sit amet, consectetuer adipiscing elit, sed diam nonummy nibh euismod tincidunt sit amet, consectetuer adipiscing elit sit amet, consectetuer adipiscing elit.</p>

  <!-- stat 1 -->
  <section class="panel" style="left:290px;top:803px;width:552px;height:268px">
    <div class="panel-head">
      <svg width="16" height="14" viewBox="0 0 16 14" fill="none" stroke="#57aad4" stroke-width="1.3"><path d="M1 2h2M1 7h2M1 12h2M6 2h9M6 7h9M6 12h9"/></svg>Stat 1
    </div>
    <div class="search" style="left:305px;top:61px;width:230px">Search
      <svg width="15" height="15" viewBox="0 0 15 15" fill="none" stroke="#b5bac0" stroke-width="1.2"><circle cx="6.5" cy="6.5" r="5"/><path d="M10 10l4 4"/></svg>
    </div>
    <table class="grid" style="left:20px;top:96px;width:512px">
      <thead><tr>
        <th style="width:145px"><span class="sort">▲<br>▼</span>Name</th>
        <th style="width:124px"><span class="sort">▲<br>▼</span>Position</th>
        <th style="width:149px"><span class="sort">▲<br>▼</span>Start Date</th>
        <th><span class="sort">▲<br>▼</span>Salary</th>
      </tr></thead>
      <tbody>
        <tr><td>Gerda</td><td>Chefin</td><td>1-11-2013</td><td>Salami</td></tr>
        <tr><td>Gerda</td><td>Chefin</td><td>2-11-2013</td><td>Salami</td></tr>
        <tr><td>Gerda</td><td>Chefin</td><td>3-11-2013</td><td>Salami</td></tr>
        <tr><td>Gerda</td><td>Chefin</td><td>4-11-2013</td><td>Salami</td></tr>
        <tr><td>Gerda</td><td>Chefin</td><td>5-11-2013</td><td>Salami</td></tr>
      </tbody>
    </table>
    <div class="entries" style="left:21px;top:239px">Showing 1 to 5 of 9 entries</div>
    <div class="pager" style="left:456px;top:237px"><span class="arrow">‹</span><span class="active">1</span><span>2</span><span>3</span><span class="next">›</span></div>
  </section>
  <p class="note" style="left:290px;top:1083px;width:540px">Lorem ipsum dolor sit amet, consectetuer adipiscing elit, sed diam nonummy nibh euismod tincidunt sit amet, consectetuer adipiscing elit sit amet, consectetuer adipiscing elit.</p>

  <!-- stat 2 -->
  <section class="panel" style="left:290px;top:1126px;width:552px;height:267px">
    <div class="panel-head">
      <svg width="16" height="14" viewBox="0 0 16 14" fill="none" stroke="#57aad4" stroke-width="1.3"><path d="M1 2h2M1 7h2M1 12h2M6 2h9M6 7h9M6 12h9"/></svg>Stat 2
    </div>
    <div class="search" style="left:305px;top:61px;width:230px">Search
      <svg width="15" height="15" viewBox="0 0 15 15" fill="none" stroke="#b5bac0" stroke-width="1.2"><circle cx="6.5" cy="6.5" r="5"/><path d="M10 10l4 4"/></svg>
    </div>
    <table class="grid" style="left:20px;top:95px;width:512px">
      <thead><tr>
        <th style="width:145px"><span class="sort">▲<br>▼</span>Domain</th>
        <th style="width:124px"><span class="sort">▲<br>▼</span>Niveau</th>
        <th style="width:149px"><span class="sort">▲<br>▼</span>Keywords</th>
        <th><span class="sort">▲<br>▼</span>SE Keywords</th>
      </tr></thead>
      <tbody>
        <tr><td>domain1.de</td><td><div class="bar"><i style="width:28%"></i></div></td><td>Gemeinsame Keywords</td><td>SE Keywords</td></tr>
        <tr><td>domain1.de</td><td><div class="bar"><i style="width:44%"></i></div></td><td>Gemeinsame Keywords</td><td>SE Keywords</td></tr>
        <tr><td>domain1.de</td><td><div class="bar"><i style="width:54%"></i></div></td><td>Gemeinsame Keywords</td><td>SE Keywords</td></tr>
        <tr><td>domain1.de</td><td><div class="bar"><i style="width:70%"></i></div></td><td>Gemeinsame Keywords</td><td>SE Keywords</td></tr>
        <tr><td>domain1.de</td><td><div class="bar"><i style="width:85%"></i></div></td><td>Gemeinsame Keywords</td><td>SE Keywords</td></tr>
      </tbody>
    </table>
    <div class="entries" style="left:21px;top:238px">Showing 1 to 5 of 9 entries</div>
    <div class="pager" style="left:456px;top:236px"><span class="arrow">‹</span><span class="active">1</span><span>2</span><span>3</span><span class="next">›</span></div>
  </section>
  <p class="note" style="left:290px;top:1405px;width:540px">Lorem ipsum dolor sit amet, consectetuer adipiscing elit, sed diam nonummy nibh euismod tincidunt sit amet, consectetuer adipiscing elit sit amet, consectetuer adipiscing elit.</p>

  <!-- right column -->
  <a class="tile tile-red" style="left:867px;top:151px">
    <svg width="22" height="32" viewBox="0 0 22 32" fill="none" stroke="#fff" stroke-width="1.6" style="margin-top:20px"><circle cx="11" cy="7" r="5"/><path d="M2 30V20a5 5 0 0 1 5-5h8a5 5 0 0 1 5 5v10zM8 16l3 6 3-6M11 22v8"/></svg>
    <h3>Profil</h3><p>Profil bearbeiten</p>
    <div class="foot"><span>WEITER</span><svg width="10" height="10" viewBox="0 0 10 10" fill="none" stroke="#fff"><circle cx="5" cy="5" r="4.3"/><path d="M4 3l2 2-2 2"/></svg></div>
  </a>
  <a class="tile tile-cyan" style="left:1011px;top:151px">
    <svg width="40" height="30" viewBox="0 0 40 30" fill="none" stroke="#fff" stroke-width="1.6" style="margin-top:22px"><circle cx="20" cy="6" r="5"/><circle cx="8" cy="9" r="4"/><circle cx="32" cy="9" r="4"/><path d="M11 28v-6a5 5 0 0 1 5-5h8a5 5 0 0 1 5 5v6zM1 26v-4a4 4 0 0 1 4-4h4M39 26v-4a4 4 0 0 0-4-4h-4"/></svg>
    <h3>Patienten</h3><p>Patienten verwalten</p>
    <div class="foot"><span>ALLE ANSEHEN</span><svg width="10" height="10" viewBox="0 0 10 10" fill="none" stroke="#fff"><circle cx="5" cy="5" r="4.3"/><path d="M4 3l2 2-2 2"/></svg></div>
  </a>
  <p class="note" style="left:867px;top:283px;width:220px">Lorem ipsum dolor sit amet, consectetuer adipiscing elit, sed diam nonummy nibh euismod tincidunt</p>

  <section class="panel" style="left:867px;top:327px;width:264px;height:162px">
    <div class="panel-head">
      <svg width="16" height="13" viewBox="0 0 16 13" fill="none" stroke="#57aad4" stroke-width="1.3"><rect x=".7" y=".7" width="14.6" height="11.6"/><path d="M3 10l4-4 2 2 2-2 3 3M10 4h2"/></svg>Willkommen:&nbsp;<strong style="font-weight:600">Dr. Mustermann</strong>
    </div>
    <p class="welcome-text">Lorem ipsum dolor sit amet, consectetuer adipiscing elit, sed diam nonummy nibh euismod tincidunt ut laoreet dolore magna aliquam erat volutpat. Ut wisi enim ad minim veniam, quis nostrud exerci tation ullamcorper suscipit lobortis nisl ut aliquip ex ea commodo consequat. Wisi enim ad minim veniam.</p>
    <div class="btn" style="left:192px;top:129px;width:54px;height:17px">Alles OK</div>
  </section>
  <p class="note" style="left:867px;top:503px;width:220px">Lorem ipsum dolor sit amet, consectetuer adipiscing elit, sed diam nonummy nibh euismod tincidunt</p>

  <section class="panel" style="left:867px;top:547px;width:264px;height:284px">
    <div class="panel-head">
      <svg width="16" height="14" viewBox="0 0 16 14" fill="none" stroke="#57aad4" stroke-width="1.3"><path d="M1 1h14M1 5h10M1 9h14M1 13h8"/></svg>Sternchen
    </div>
    <div class="search" style="left:17px;top:60px;width:230px">Search
      <svg width="15" height="15" viewBox="0 0 15 15" fill="none" stroke="#b5bac0" stroke-width="1.2"><circle cx="6.5" cy="6.5" r="5"/><path d="M10 10l4 4"/></svg>
    </div>
    <table class="grid" style="left:17px;top:94px;width:230px">
      <thead><tr>
        <th style="width:88px"><span class="sort">▲<br>▼</span>Name</th>
        <th style="width:77px"><span class="sort">▲<br>▼</span>Profilseite</th>
        <th><span class="sort">▲<br>▼</span>Bewertung</th>
      </tr></thead>
      <tbody>
        <tr><td><span class="chev">›</span><a>Vela!</a></td><td><span class="chev">›</span><a>Xyz Ungelot</a></td><td class="stars">☆☆☆☆☆</td></tr>
        <tr><td><span class="chev">›</span><a>Kliniq.de</a></td><td><span class="chev">›</span><a>Xyz Ungelot</a></td><td class="stars">☆☆☆</td></tr>
        <tr><td><span class="chev">›</span><a>Die Praxiswahl</a></td><td><span class="chev">›</span><a>Xyz Ungelot</a></td><td class="stars">☆☆☆☆</td></tr>
        <tr><td><span class="chev">›</span><a>MedSpot</a></td><td><span class="chev">›</span><a>Xyz Ungelot</a></td><td class="stars">☆☆☆☆☆</td></tr>
        <tr><td><span class="chev">›</span><a>Vitaloo</a></td><td><span class="chev">›</span><a>Xyz Ungelot</a></td><td class="stars">☆☆☆</td></tr>
        <tr><td><span class="chev">›</span><a>Vitaloo</a></td><td><span class="chev">›</span><a>Xyz Ungelot</a></td><td class="stars">☆☆☆☆☆</td></tr>
      </tbody>
    </table>
    <div class="entries" style="left:23px;top:255px">Showing 1 to 6 of 20 entries</div>
    <div class="pager" style="left:170px;top:253px"><span class="arrow">‹</span><span class="active">1</span><span>2</span><span>3</span><span class="next">›</span></div>
  </section>
  <p class="note" style="left:867px;top:845px;width:220px">Lorem ipsum dolor sit amet, consectetuer adipiscing elit, sed diam nonummy nibh euismod tincidunt</p>

  <footer class="footer">
    <span class="copy">©2014 - All rights Reserved, Praxora Admin</span>
    <span class="brand">Praxora Admin</span>
  </footer>
</div>
</body>
</html>
```